4th Generation Family Business Needs a New Card Design!

We are a family owned 4th Generation company. We are based in the Sydney, Australia area and we are desperately in need of a more modern and classy card. We are monumental masons who design, supply & erect lasting memorials throughout cemeteries in Sydney. Our customers are normally in a period of grieving. I have attached logo files that will need to be implemented on the card. Company was established 1935. Australian Owned and Operated. Card needs to be designed to PRINTLY.com specification.

Target Market(s)

Our target market is based upon people that a grieving for family members that have passed away. We also deal with alot of companies that own and operate cemeteries.

Industry/Entity Type

Business

Contact Information for Business Card

Oliver Brantley, Operations Manager, 0417552908, oliver@hollowaystoneworks.com.au
Martin Brantley, Director, 0431906627, martin@hollowaystoneworks.com.au
Phone # 02 9634 2258
Website: www.hollowaystoneworks.com.au
Address: Suite 17, 8 Calloway Lane, East Penrose, Sydney NSW 2290

Font styles to use
Serif
Decorative
Script

Requirements
Must have
• Would like to see the logo nicely implemented with a modern design. Embossed lettering would be a nice additive.

```html
<!DOCTYPE html>
<html lang="en">
<head>
<meta charset="utf-8">
<title>Holloway Stoneworks – Business Card</title>
<link href="https://fonts.googleapis.com/css2?family=Roboto+Slab:wght@400;700&display=swap" rel="stylesheet">
<style>
  :root {
    --stage: #eceeed;
    --paper: #ffffff;
    --gold: #efc04d;
    --slate: #343a43;
    --ink: #1f1f1f;
    --line: #e2b43e;
  }
  * { box-sizing: border-box; margin: 0; padding: 0; }
  html, body {
    width: 1200px; height: 1000px; overflow: hidden;
    background: var(--stage);
    font-family: "Roboto Slab", Georgia, serif;
    color: var(--ink);
  }
  .stage {
    position: relative; width: 1200px; height: 1000px;
  }
  .card {
    position: absolute; left: 320px;
    width: 560px; height: 320px;
    box-shadow: 0 6px 18px rgba(0,0,0,0.12);
    overflow: hidden;
  }
  .card--front { top: 150px; display: flex; background: var(--paper); }
  .card--back {
    top: 530px; background: var(--slate);
    display: flex; align-items: center; justify-content: center;
  }

  .front__brand {
    position: relative; width: 46%; height: 100%;
    display: flex; flex-direction: column; align-items: center; justify-content: center;
  }
  .front__details {
    width: 54%; height: 100%;
    background: var(--gold);
    padding: 34px 30px 0 34px;
  }

  .wordmark {
    display: flex; flex-direction: column; align-items: center; gap: 12px;
  }
  .wordmark__square {
    width: 26px; height: 26px; background: var(--ink);
  }
  .wordmark__name {
    font-weight: 400; font-size: 24px; line-height: 1.15;
    letter-spacing: 2px; text-transform: uppercase; text-align: center;
    color: var(--ink);
  }
  .wordmark__rule {
    width: 150px; height: 1px; background: var(--line);
  }

  .card--back .wordmark__square { width: 40px; height: 40px; background: var(--paper); }
  .card--back .wordmark__name { color: var(--paper); font-size: 36px; letter-spacing: 3px; }
  .card--back .wordmark__rule { width: 230px; background: var(--paper); opacity: 0.7; }

  .website {
    position: absolute; left: 24px; bottom: 22px;
    font-size: 11px; font-weight: 700; letter-spacing: 0.2px;
  }

  .person__name { font-size: 19px; font-weight: 700; }
  .person__role { font-size: 12px; margin-top: 4px; }
  .contact { margin-top: 70px; font-size: 11px; line-height: 1.65; }
  .contact__label { margin-bottom: 2px; }
</style>
</head>
<body>
<main class="stage">

  <section class="card card--front" aria-label="Business card front">
    <div class="front__brand">
      <div class="wordmark">
        <span class="wordmark__square"></span>
        <span class="wordmark__name">Holloway<br>Stoneworks</span>
        <span class="wordmark__rule"></span>
      </div>
      <p class="website">www.hollowaystoneworks.com.au</p>
    </div>
    <div class="front__details">
      <h1 class="person__name">Oliver Brantley</h1>
      <p class="person__role">Operation Manager (0417552908)</p>
      <div class="contact">
        <p class="contact__label">Contact:</p>
        <p>02 9634 2258</p>
        <p>oliver@hollowaystoneworks.com.au</p>
        <p>Suite 17, 8 Calloway Lane, East Penrose, Sydney NSW 2290</p>
      </div>
    </div>
  </section>

  <section class="card card--back" aria-label="Business card back">
    <div class="wordmark">
      <span class="wordmark__square"></span>
      <span class="wordmark__name">Holloway<br>Stoneworks</span>
      <span class="wordmark__rule"></span>
    </div>
  </section>

</main>
</body>
</html>
```